Judge Whitlock's Mill Jubilee BBQ

We need a flyer promoting a BBQ, music, and community conversation campaign event that is happening in conjunction with a larger community event "Mill Jubilee" It is for the Re Elect Judge Peter Whitlock campaign, all are invited. We would like the design to be very Americana, and feature the Judge's name at the top or near the top. Play with the slogans "Shade Trees and Sweet Tea, BBQ and Music, Time to Visit and Talk" and "Judge Whitlocks Mill Jubilee BBQ Bash: Music, Politics and Community"

```html
<!DOCTYPE html>
<html lang="en">
<head>
<meta charset="utf-8">
<title>Judge Whitlock's Mill Jubilee BBQ Bash</title>
<link rel="stylesheet" href="https://fonts.googleapis.com/css2?family=Archivo+Black&family=Bebas+Neue&family=Roboto+Slab:wght@400;700&family=Ultra&display=swap">
<style>
  :root {
    --navy: #0c3f4f;
    --red: #bb2834;
    --cream: #fefee2;
  }
  html, body {
    margin: 0;
    padding: 0;
    overflow: hidden;
    background: var(--navy);
  }
  .flyer {
    position: relative;
    width: 923px;
    height: 1200px;
    background: var(--navy);
    overflow: hidden;
  }
  .frame {
    position: absolute;
    left: 32px; top: 38px;
    width: 834px; height: 1112px;
    border: 11px solid var(--red);
    background: var(--cream);
  }
  .invite-tab {
    position: absolute;
    left: 218px; top: 38px;
    width: 484px; height: 43px;
    display: flex; align-items: center; justify-content: center;
    font-family: "Archivo Black", sans-serif;
    font-size: 25px;
    letter-spacing: 3px;
    color: var(--cream);
  }
  .invite-tab svg { position: absolute; inset: 0; z-index: 0; }
  .invite-tab span { position: relative; z-index: 1; }
  .candidate {
    position: absolute;
    margin: 0;
    left: 0; right: 0; top: 124px;
    text-align: center;
    font-family: "Bebas Neue", sans-serif;
    font-weight: 400;
    font-size: 96px;
    letter-spacing: -1px;
    line-height: 1;
    color: var(--navy);
    white-space: nowrap;
  }
  .event-title {
    position: absolute;
    left: 0; right: 0;
    text-align: center;
    font-family: "Ultra", serif;
    line-height: 1;
    white-space: nowrap;
  }
  .event-title--first {
    top: 240px;
    font-size: 132px;
    color: var(--navy);
    text-shadow: 4px 4px 0 var(--cream), 7px 7px 0 var(--navy);
  }
  .event-title--second {
    top: 366px;
    font-size: 100px;
    color: var(--red);
    text-shadow: 4px 4px 0 var(--cream), 7px 7px 0 var(--red);
  }
  .utensil {
    position: absolute;
    border-radius: 40px;
    background: linear-gradient(135deg, rgba(12,63,79,0.18), rgba(12,63,79,0.08));
  }
  .utensil--spatula { left: 92px; top: 285px; width: 128px; height: 162px; }
  .utensil--fork { left: 696px; top: 308px; width: 124px; height: 172px; }
  .ribbon {
    position: absolute;
    left: 123px; top: 484px;
    width: 682px; height: 90px;
  }
  .bash-box {
    position: absolute;
    left: 158px; top: 607px;
    width: 604px; height: 212px;
    border: 1px dashed var(--navy);
    display: flex; flex-direction: column; align-items: center; justify-content: center;
    font-family: "Bebas Neue", sans-serif;
    font-size: 50px;
    line-height: 47px;
    letter-spacing: 2.5px;
    color: var(--navy);
  }
  .bash-box .highlight { color: var(--red); }
  .when {
    position: absolute;
    left: 0; right: 0; top: 842px;
    text-align: center;
    font-family: "Roboto Slab", serif;
    font-weight: 700;
    font-size: 28px;
    letter-spacing: 5px;
    color: var(--navy);
  }
  .pin {
    position: absolute;
    left: 423px; top: 905px;
    width: 52px; height: 54px;
  }
  .directions {
    position: absolute;
    left: 0; right: 0; top: 972px;
    text-align: center;
    font-family: "Roboto Slab", serif;
    font-weight: 700;
    font-size: 32px;
    letter-spacing: 3px;
    color: var(--navy);
    white-space: nowrap;
  }
  .address {
    position: absolute;
    left: 0; right: 0; top: 1022px;
    text-align: center;
    font-family: "Roboto Slab", serif;
    font-size: 20px;
    letter-spacing: 3px;
    color: var(--navy);
    white-space: nowrap;
  }
  .website {
    position: absolute;
    left: 0; right: 0; top: 1066px;
    text-align: center;
    font-family: "Archivo Black", sans-serif;
    font-size: 27px;
    letter-spacing: 2.5px;
    color: var(--red);
  }
</style>
</head>
<body>
<main class="flyer">
  <div class="frame"></div>

  <div class="invite-tab">
    <svg width="484" height="43" viewBox="0 0 484 43" aria-hidden="true">
      <polygon points="0,0 484,0 462,43 22,43" fill="var(--red)"/>
    </svg>
    <span>ALL ARE INVITED TO</span>
  </div>

  <h1 class="candidate">JUDGE PETER WHITLOCK</h1>

  <div class="utensil utensil--spatula" role="img" aria-label="Grill spatula illustration"></div>
  <div class="utensil utensil--fork" role="img" aria-label="Grill fork illustration"></div>

  <div class="event-title event-title--first">MILL</div>
  <div class="event-title event-title--second">JUBILEE</div>

  <svg class="ribbon" viewBox="0 0 682 90" aria-label="BBQ Bash">
    <polygon points="0,0 125,0 125,72 0,72 18,36" fill="var(--red)"/>
    <polygon points="682,0 557,0 557,72 682,72 664,36" fill="var(--red)"/>
    <polygon points="125,0 175,0 175,18 73,18" fill="var(--cream)"/>
    <polygon points="557,0 507,0 507,18 609,18" fill="var(--cream)"/>
    <rect x="73" y="18" width="536" height="72" fill="var(--navy)"/>
    <text x="341" y="75" text-anchor="middle" font-family="Archivo Black, sans-serif" font-size="56" letter-spacing="12" fill="var(--cream)">BBQ BASH</text>
  </svg>

  <section class="bash-box">
    <div>MUSIC, POLITICS &amp; COMMUNITY</div>
    <div>PICKIN' GRILLIN' &amp; POLITIKIN</div>
    <div class="highlight">UNLIMITED SHADE TREES</div>
    <div>AND SWEET TEA</div>
  </section>

  <div class="when">JUNE 8TH | FROM 10AM - 2PM</div>

  <svg class="pin" viewBox="0 0 52 54" aria-hidden="true">
    <path d="M26 2 C15 2 8 10 8 19 C8 30 26 44 26 44 C26 44 44 30 44 19 C44 10 37 2 26 2 Z" fill="var(--navy)"/>
    <circle cx="26" cy="19" r="7" fill="var(--cream)"/>
    <path d="M12 40 C4 43 4 49 14 51 C22 53 30 53 38 51 C48 49 48 43 40 40" fill="none" stroke="var(--navy)" stroke-width="4"/>
  </svg>

  <div class="directions">FOLLOW THE TRAIN DOWN WEST MILL</div>
  <div class="address">418 WEST MILL STREET HARLAN SPRINGS, ALABAMA</div>
  <div class="website">JUDGEPETERWHITLOCK.COM</div>
</main>
</body>
</html>
```